International Trading Company, 'KIRO' needs a Business Card

The company name is "KIRO" and it has own logo design.
I'd like to use its logo on this business card.
I need two side Business Card.
I'll look forward to your great design.
Thank you very much in advance.

Contact Information for Business Card

Company Name : Kiro Harbour Limited
Information Example
Dorian Pallister
Mobile(use icon please) : 1 (212) 555-0143
Tel(use icon please) : 1 (212) 555-0178
Email(use icon please) : dorian27@kiroharbour-mail.com
Address(use icon please) : 482 Halden Ave, New York, NY 10160, USA

```html
<!DOCTYPE html>
<html lang="en">
<head>
<meta charset="utf-8">
<title>Kiro Harbour Limited – Business Card</title>
<link rel="stylesheet" href="https://fonts.googleapis.com/css2?family=Abril+Fatface&family=Arimo&family=Karla:wght@400;700&display=swap">
<style>
  :root {
    --paper: #ffffff;
    --ink: #000000;
    --graphite: #555556;
    --silver: #d4d4d4;
    --logo-grey: #58585a;
  }
  * { margin: 0; padding: 0; box-sizing: border-box; }
  html, body { width: 848px; height: 1200px; overflow: hidden; background: var(--paper); }
  .canvas { position: relative; width: 848px; height: 1200px; background: var(--paper); overflow: hidden; }
  .decor { position: absolute; inset: 0; width: 848px; height: 1200px; }

  .brand-name {
    position: absolute; left: 96px; top: 160px; width: 612px;
    font-family: "Karla", sans-serif; font-weight: 700;
    font-size: 178px; line-height: 1; letter-spacing: 6px;
    color: var(--logo-grey); text-align: center;
  }
  .brand-legal {
    position: absolute; left: 96px; top: 331px; width: 612px;
    font-family: "Karla", sans-serif; font-weight: 400;
    font-size: 27px; letter-spacing: 1px;
    color: var(--logo-grey); text-align: center;
  }

  .person-name {
    position: absolute; left: 36px; top: 760px; width: 240px;
    font-family: "Abril Fatface", serif; font-size: 50px; line-height: 76px;
    color: var(--ink); text-align: center;
  }

  .contact {
    position: absolute; font-family: "Arimo", sans-serif; color: var(--ink);
    white-space: nowrap;
  }
  .contact--phone { font-size: 29px; word-spacing: 8px; }
  .contact--mobile { left: 541px; top: 686px; }
  .contact--tel { left: 541px; top: 802px; }
  .contact--email { left: 516px; top: 962px; font-size: 19px; }
  .contact--address {
    left: 486px; top: 1088px; width: 340px; text-align: center;
    font-size: 21px; line-height: 27px; word-spacing: 6px; white-space: normal;
  }
</style>
</head>
<body>
<main class="canvas">
  <svg class="decor" viewBox="0 0 848 1200" aria-hidden="true">
    <defs>
      <clipPath id="back-side"><rect x="0" y="600" width="848" height="600"/></clipPath>
    </defs>
    <!-- front side edge -->
    <path d="M776 0 C800 150 806 300 800 594 L848 594 L848 0 Z" fill="var(--graphite)"/>
    <path d="M812 0 C822 200 800 400 792 594 L848 594 L848 0 Z" fill="var(--ink)"/>
    <!-- back side wave -->
    <g clip-path="url(#back-side)" fill="none">
      <path transform="translate(31 0)" d="M300 570 C370 660 370 760 345 880 S272 1100 278 1220" stroke="var(--silver)" stroke-width="62"/>
      <path transform="translate(23 0)" d="M300 570 C370 660 370 760 345 880 S272 1100 278 1220" stroke="var(--graphite)" stroke-width="46"/>
      <path transform="translate(14 0)" d="M300 570 C370 660 370 760 345 880 S272 1100 278 1220" stroke="var(--ink)" stroke-width="28"/>
    </g>
    <!-- mobile icon -->
    <g class="icon-mobile">
      <rect x="456" y="654" width="47" height="78" rx="4" fill="var(--ink)"/>
      <rect x="461" y="661" width="37" height="60" fill="var(--paper)"/>
      <circle cx="479.5" cy="726" r="2.6" fill="var(--paper)"/>
    </g>
    <!-- telephone icon -->
    <path class="icon-tel" d="M452 782 c-8 6 -12 14 -8 26 c8 22 26 40 48 48 c12 4 20 0 26 -8 l-16 -16 c-5 4 -10 6 -14 4 c-10 -5 -20 -15 -25 -25 c-2 -4 0 -9 4 -14 z"
      fill="none" stroke="var(--ink)" stroke-width="4" stroke-linejoin="round"/>
    <!-- email icon -->
    <g class="icon-email" fill="none" stroke="#333" stroke-width="6" stroke-linejoin="round">
      <rect x="409" y="944" width="77" height="52" rx="7"/>
      <path d="M416 952 L447.5 980 L479 952"/>
    </g>
    <!-- location pin -->
    <path class="icon-pin" d="M428 1140 C412 1118 402 1104 402 1092 a26 26 0 0 1 52 0 c0 12 -10 26 -26 48 z M428 1080 a11 11 0 1 0 0.01 0 z"
      fill="var(--ink)" fill-rule="evenodd"/>
  </svg>

  <div class="brand-name">KIRO</div>
  <div class="brand-legal">Kiro Harbour Limited</div>

  <h1 class="person-name">Dorian<br>Pallister</h1>

  <p class="contact contact--phone contact--mobile">1 (212) 555-0143</p>
  <p class="contact contact--phone contact--tel">1 (212) 555-0178</p>
  <p class="contact contact--email">dorian27@kiroharbour-mail.com</p>
  <p class="contact contact--address">482 Halden Ave, New York, NY<br>10160, USA</p>
</main>
</body>
</html>
```